Lively Ledgers - Minimalistic Single Page Web Design

Project: We are in the process of creating a new Corp Identity. Design a website for our company incorporating the Logo recently designed and selected from a ArtMarketo contest. (attached)

Designers: For this project, you need to design a minimalistic single page, modern website. Beside text and image placement, you will also need to describe user interface, how content is presented and so on.
- Design Layout
- Design Image placements (if any)
- Design menu and buttons
- Design menu and buttons placements
- Design content layout
- Design overall effect and feel of website
- Design color scheme
- Design content style (tone and style of content, words type, how much)
- Design user interface (how do you scroll, what happens when you mouseover buttons, where do certain links and buttons lead you)

Coding Requirements: You need to design the website with a modern perspective on website visuals and effects. Jquery, HTML5 (no FLASH please). You do not need to code for this particular contest, but if you can also code, great, tell me and let me know how I can hire you to complete it. If you know someone that can code your vision, great, let me know. If not, you need to be clear and concise, and be willing to help me communicate with a developer to get the site executed. The web site needs to be modern and dynamic.

Company Name:
Lively Ledgers; Lively-Ledgers; LivelyLedgers

Domain: www.lively-ledgers.com

Company Industry:
Lively Ledgers provides consulting in areas of finance, accounting, business organization, and set up.
- Bookkeeping
- Project Management
- Budget Management
- Cash Management
- Receipt Management
- Filing and Records Management
- Training of administration and accounting staff
- Financial Reports
- Spreadsheets
- Graphs, charts and trend analysis
- Business set up
- Tax filings
- Payroll and HR

Clients:
- Small to medium size businesses
- Proprietors
- Entrepreneurs
- Mom & Pops Shops
- We cater to every industry

Corporate Identity:
- Past: I have never complete a webpage for my company. I did scratch several projects that were started and never completed. I fell in love with stick figures, whimsical designs, similar to that of "Cloudvat", I believed in simplicity and minimalism. However, I was not effective in find the right people to complete my project. Bits and pieces of the website was designed, but never executed.

- Current: I need a webpage design. The web design must align with the current logo aesthetics.The current logo is new. I selected this logo for its simplicity and modern feel. It also incorporated an image of a trending graph, which fits with my company's profile. Still, I am leaning towards simple design, minimalism with boldness. I like my new webpage to be mature and professional, but I want it to portray energy and youth. So no "traditional corp" like design. I like new HTML5 elements, jquery and fun and beautiful forms and buttons. Less image is more.

Note: Please improvise according to your taste and professional perspective, you do not have to follow my suggestions word for word.

Features & Layout:
- Single page layout
- Vertical scroll
- Framed sections so that it looks good on the screen
- Well designed and strategically placed menu bar
- Fills a modern browser
- Beautiful color scheme that pops
- Incorporate Logo aesthetics

Fonts and Type:
- This is an element of the overall design
- I love clean fonts
- Fonts that adds meaning to the overall effect
- Clean

Sounds
- Please no cheesy sounds and background music

Images:
- To your liking
- But please, no lame corp people in suits
- No lame photographs
- I like stick figures
- I like whimsical illustrations

Landing Page:
- This should be the bulk of your design
- The landing page must be impressive, eye catchy
- Bold

Menu Bar:
- Header (introduction and landing page)
- Service & Products
- Company (about us)
- Affiliates and Clients (reference area)
- Contact (contact us area)
- Footer

Colors:
- Up to you, I just like things clean and easy to read
- No black background behind text
- Incorporate Logo Colors

Web Effects:
- According to your liking
- You will need to be involve to communicate the layout and design to the developer, so you need to be clear in your design.

Content:
- You personally don't have to come up with the content, but if you can great.
- I will help come up with the content throughout the contect timeframe, just let me know what you want
- I do not like too much content in my website. The most for each section is 2-3 lines if any.
- Combination could also be one liners.
- I like minimalistic approach.
- If you are not creating the final content, you need to show what type of content need to be created and in what style or tone.

Samples and Inspirations:
- http://singlesheetgallery.example/
- http://vantorix.example/#top
- http://brightmopservices.example/#about
- http://layoutjournal.example/inspiration/23-inspiring-single-page-designs
- http://www.kelvarstudio.example/
- http://www.dariuskessley.example/

This I do not want:
- Too much popups (none if possible)
- Images of people
- Images of people in suits
- Stereotypical images of accountants
- Scrolling marquee
- Clip arts
Updates

Designers, I want to stress the fact that I am looking for a design, not simply a website. The website is 1 page long. Text and content should be minimal. So this means that the design has to do most of the talking. Please do not submit template like web designs, I can pull this off myself if needed. I need you to design a great header, footer and the connecting tissue from landing to end of the page. The entire design needs to flow.

Again, please do not use images of corp people or anything like that. Please think outside the box in how you want to express the company.

Some ideas:
An illustration from beginning to end of the website, have a story.
Add colors to the back ground. 
The background should not get in the way of reading the text, but it does not have to be boring.
Be bold in your design.

Also, please describe more about your design when you submit. Please don't submit a template like design and have no explanation for your actions.

Also, fee free to ask me questions. I am here to help. I check this everyday, so please contact if you need anything.

Designers, please read the details of my post before you submit the design.

If you have a great concept idea but is worry, you can go ahead and submit a pencil draft and ask my opinion before you work anymore on it.

Please see the website samples below for what I am really looking for:

Reason: Hi everyone, I am extending the deadline. It looks like some design are still pending completion, and I want you to have enough time to work on it.

```html
<!DOCTYPE html>
<html lang="en">
<head>
<meta charset="utf-8">
<title>Lively Ledgers</title>
<link rel="stylesheet" href="https://fonts.googleapis.com/css2?family=Advent+Pro:wght@400&family=Comfortaa:wght@400&family=Open+Sans:wght@400;600&display=swap">
<style>
  :root {
    --green-top: #7d9a52;
    --green-mid: #9bb862;
    --nav-home: #4f5bff;
    --nav-services: #3a44c8;
    --nav-company: #2e3399;
    --nav-affiliates: #232673;
    --nav-contact: #1a1b50;
    --brand-blue: #2b2f8a;
    --ink: #1e1e1e;
    --bg-light: #fbfbfb;
    --bg-dark: #dcdcdc;
    --footer: #000;
  }
  * { margin: 0; padding: 0; box-sizing: border-box; }
  html, body { width: 1200px; height: 720px; overflow: hidden; }
  body {
    position: relative;
    font-family: "Open Sans", sans-serif;
    background: radial-gradient(ellipse 60% 70% at 55% 55%, var(--bg-light), var(--bg-dark));
  }
  .sidebar {
    position: absolute; left: 0; top: 0; width: 94px; height: 720px;
    background: linear-gradient(90deg, var(--green-top), var(--green-mid));
    border-right: 1px solid #fff;
  }
  .nav { position: absolute; top: 107px; left: 0; width: 94px; list-style: none; }
  .nav-item {
    height: 95px; display: flex; flex-direction: column; align-items: center; justify-content: center;
    color: #fff; font-size: 15px; line-height: 17px; text-align: center;
    text-shadow: 0 1px 2px rgba(0,0,0,.5);
  }
  .nav-item svg { width: 40px; height: 36px; margin-bottom: 4px; fill: #fff; }
  .nav-home { background: var(--nav-home); }
  .nav-services { background: var(--nav-services); }
  .nav-company { background: var(--nav-company); }
  .nav-affiliates { background: var(--nav-affiliates); }
  .nav-contact { background: var(--nav-contact); }

  .brand {
    position: absolute; left: 94px; width: 1106px; top: 36px; text-align: center;
    font-family: "Comfortaa", sans-serif; font-size: 44px; color: var(--brand-blue); letter-spacing: 1px;
  }
  .header-rule {
    position: absolute; left: 230px; width: 840px; top: 130px; height: 2px;
    background: linear-gradient(90deg, transparent, rgba(0,0,0,.12), transparent);
  }
  .header-notch { position: absolute; left: 613px; top: 128px; width: 36px; height: 16px; }

  .headline {
    position: absolute; left: 94px; width: 1106px; top: 188px; text-align: center;
    font-family: "Advent Pro", sans-serif; font-weight: 400; font-size: 34px; letter-spacing: .5px;
    color: #222; text-transform: uppercase;
    text-shadow: 1px 1px 0 #fff, 0 2px 3px rgba(0,0,0,.2);
  }
  .community-art {
    position: absolute; left: 216px; top: 283px; width: 324px; height: 292px;
    border-radius: 48% 52% 44% 48% / 50% 50% 46% 52%;
    background: radial-gradient(circle at 40% 45%, #f2b04a, #e46c8e 40%, #3fa6d6 70%, #8bbf3f);
    opacity: .85;
  }
  .community-shadow {
    position: absolute; left: 295px; top: 606px; width: 200px; height: 10px; border-radius: 50%;
    background: radial-gradient(ellipse, rgba(70,90,120,.35), transparent 70%);
  }
  .intro { position: absolute; left: 593px; top: 307px; width: 406px; }
  .intro p {
    font-size: 14px; line-height: 20.4px; color: var(--ink); text-align: justify; margin-bottom: 32px;
  }
  .footer {
    position: absolute; right: 0; bottom: 0; width: 229px; height: 33px;
    background: var(--footer); clip-path: polygon(18px 0, 100% 0, 100% 100%, 0 100%);
    color: #fff; font-size: 14px; font-weight: 600; line-height: 33px; padding-left: 28px;
  }
</style>
</head>
<body>
  <aside class="sidebar">
    <ul class="nav">
      <li class="nav-item nav-home">
        <svg viewBox="0 0 40 36"><path d="M20 3 L37 18 L33 18 L33 33 L24 33 L24 23 L16 23 L16 33 L7 33 L7 18 L3 18 Z"/></svg>
        Home
      </li>
      <li class="nav-item nav-services">
        <svg viewBox="0 0 40 36"><circle cx="15" cy="14" r="10" fill="none" stroke="#fff" stroke-width="5" stroke-dasharray="4 2.3"/><circle cx="29" cy="27" r="6" fill="none" stroke="#fff" stroke-width="4" stroke-dasharray="3 1.8"/></svg>
        Services<br>&amp; Products
      </li>
      <li class="nav-item nav-company">
        <svg viewBox="0 0 40 36"><circle cx="20" cy="8" r="7"/><path d="M8 36 L8 22 Q8 16 14 16 L26 16 Q32 16 32 22 L32 36 Z"/></svg>
        Company
      </li>
      <li class="nav-item nav-affiliates">
        <svg viewBox="0 0 40 36"><rect x="2" y="8" width="12" height="8" transform="rotate(30 8 12)"/><rect x="26" y="8" width="12" height="8" transform="rotate(-30 32 12)"/><path d="M10 18 L20 12 L30 18 L22 28 Z"/></svg>
        Affiliates<br>&amp; Clients
      </li>
      <li class="nav-item nav-contact">
        <svg viewBox="0 0 40 36"><rect x="3" y="8" width="34" height="22" rx="2"/><path d="M3 9 L20 22 L37 9" fill="none" stroke="#1a1b50" stroke-width="2"/></svg>
        Contact
      </li>
    </ul>
  </aside>

  <header>
    <div class="brand">livelyledgers</div>
    <div class="header-rule"></div>
    <svg class="header-notch" viewBox="0 0 36 16"><rect width="36" height="16" fill="#f4f4f4"/><path d="M12 4 L18 10 L24 4" fill="none" stroke="#444" stroke-width="3"/></svg>
  </header>

  <main>
    <h1 class="headline">Lorem ipsum dolor sit amet, consectetur</h1>
    <div class="community-art" role="img" aria-label="Colourful crowd of people icons forming a speech bubble"></div>
    <div class="community-shadow"></div>
    <section class="intro">
      <p>Ut enim ad minim veniam, quis nostrud exercitation ullamco laboris nisi ut aliquip ex ea commodo consequat. Duis aute irure dolor in reprehenderit in voluptate velit esse cillum dolore eu fugiat nulla pariatur. Excepteur sint occaecat cupidatat non proident, sunt in culpa qui officia deserunt mollit anim</p>
      <p>Ut enim ad minim veniam, quis nostrud exercitation ullamco laboris nisi ut aliquip ex ea commodo consequat. Duis aute irure dolor in reprehenderit in voluptate velit esse cillum dolore eu fugiat nulla pariatur. Excepteur sint occaecat cupidatat non proident, sunt in culpa qui officia deserunt mollit anim</p>
    </section>
  </main>

  <footer class="footer">©2013 livelyledgers</footer>
</body>
</html>
```